Flyer für Service, Wartung, Überprüfung und Reinigung von Kälte- und Klimaanlagen
Ich bin sehr zufrieden mit dem Designer! Sehr professionelle Arbeit, schnelle Umsetzung und super Kommunikation. Das Ergebnis ist genau so geworden, wie ich es mir vorgestellt habe. Klare Empfehlung – jederzeit gerne wieder!
Zielgruppe
Borvent Kälte ist ein österreichischer Fachbetrieb mit dem Schwerpunkt: Service, Wartung, Überprüfung und Reinigung von Kälte- und Klimaanlagen im Gewerbe.
Meine Zielgruppe sind vor allem Unternehmen wie Büros, Arztpraxen, Gastronomie, Shops, kleine bis mittlere Betriebe sowie Hausverwaltungen und Betreiber von gewerblichen Klimaanlagen, die eine sichere, hygienische und gesetzeskonforme Lösung suchen.
Aufgabenstellung
Der Flyer soll modern, seriös und technisch-professionell wirken (klar, sauber, gut lesbar).
Farben: Blau/Weiß/Grau, gerne mit Icons/Checkliste.
Klimaanlagen im Gewerbe – sicher, effizient und gesetzeskonform
Fachgerechte Überprüfung & Reinigung von Klimaanlagen in ganz Österreich
Hinweis zur gesetzlichen Verpflichtung:
Betreiber von Kälte- und Klimaanlagen sind verpflichtet, ihre Anlagen in einem sicheren und hygienisch einwandfreien Zustand zu halten. Die regelmäßige Überprüfung und Reinigung ergibt sich u. a. aus:

```html
<!DOCTYPE html>
<html lang="de">
<head>
<meta charset="utf-8">
<title>Borvent Kälte – Flyer</title>
<link href="https://fonts.googleapis.com/css2?family=Montserrat:wght@300;400;500;600;700;800&display=swap" rel="stylesheet">
<style>
  :root {
    --navy: #1f5673;
    --navy-deep: #163f57;
    --white: #ffffff;
    --paper: #f7f8f9;
    --grey-bg: #ececec;
    --text: #2b3540;
    --muted: #5b6770;
    --photo-wall: #8a6c4c;
    --photo-floor: #b9b9b6;
    --photo-sky: #dfe5ea;
    --photo-unit: #9aa6b0;
  }
  * { box-sizing: border-box; margin: 0; padding: 0; }
  html, body { width: 1200px; height: 800px; overflow: hidden; }
  body {
    background: var(--grey-bg);
    font-family: "Montserrat", Arial, sans-serif;
    color: var(--text);
    position: relative;
  }
  .spread {
    position: absolute;
    top: 209px;
    width: 540px;
    height: 382px;
    display: flex;
    box-shadow: 0 6px 18px rgba(0,0,0,.12);
  }
  .spread--outer { left: 30px; }
  .spread--inner { left: 630px; }
  .page {
    position: relative;
    width: 270px;
    height: 382px;
    overflow: hidden;
    background: var(--white);
  }

  /* Back cover */
  .back { background: linear-gradient(160deg, var(--navy) 0%, var(--navy-deep) 100%); color: var(--white); }
  .brand {
    position: absolute;
    display: flex;
    flex-direction: column;
    align-items: center;
    gap: 8px;
    font-weight: 700;
    letter-spacing: .06em;
    text-align: center;
  }
  .brand__dot { width: 34px; height: 34px; border-radius: 50%; background: currentColor; }
  .brand__name { font-size: 15px; line-height: 1.1; }
  .back .brand { left: 0; right: 0; top: 140px; }
  .back__address { position: absolute; left: 26px; bottom: 30px; font-size: 8px; line-height: 1.45; font-weight: 300; }
  .back__address strong { font-weight: 700; }
  .back__mail { position: absolute; right: 24px; bottom: 30px; font-size: 8px; font-weight: 300; }

  /* Front cover */
  .front__photo { position: absolute; inset: 0 0 132px 0; }
  .front__wedge { position: absolute; left: 0; top: 0; width: 270px; height: 250px; }
  .front .brand { left: 14px; top: 22px; color: var(--navy); width: 96px; }
  .front .brand__dot { width: 28px; height: 28px; }
  .front .brand__name { font-size: 11px; }
  .front__band {
    position: absolute; left: 0; right: 0; bottom: 0; height: 132px;
    background: var(--navy); color: var(--white);
    padding: 22px 20px 0 20px;
  }
  .front__title { font-size: 15px; font-weight: 800; line-height: 1.22; }
  .front__subtitle { margin-top: 8px; font-size: 9.5px; font-weight: 300; line-height: 1.35; }

  /* Inside left */
  .services { padding: 28px 20px 0 22px; background: var(--white); }
  .services__title { font-size: 11px; font-weight: 700; color: var(--navy); margin-bottom: 18px; }
  .services__grid {
    display: grid;
    grid-template-columns: repeat(3, 1fr);
    column-gap: 10px;
    row-gap: 16px;
  }
  .service { display: flex; flex-direction: column; gap: 5px; }
  .service svg { width: 26px; height: 22px; stroke: var(--navy); fill: none; stroke-width: 1.4; stroke-linecap: round; stroke-linejoin: round; }
  .service__label { font-size: 6.6px; line-height: 1.35; color: var(--text); }
  .footer {
    position: absolute; left: 0; right: 0; bottom: 0; height: 22px;
    background: var(--navy); color: var(--white);
    font-size: 6.5px; display: flex; align-items: center; padding: 0 20px;
  }
  .footer strong { font-weight: 700; margin-right: 3px; }
  .footer--right { justify-content: flex-end; }

  /* Inside right */
  .notice { background: var(--white); }
  .notice__photo { position: absolute; right: 0; bottom: 22px; width: 270px; height: 200px; }
  .notice__body { position: relative; padding: 28px 20px 0 20px; }
  .notice__title { font-size: 11.5px; font-weight: 700; color: var(--navy); margin-bottom: 8px; }
  .notice__text { font-size: 6.8px; line-height: 1.5; color: var(--text); }
  .laws { margin: 8px 0 10px; list-style: none; font-size: 7px; font-weight: 700; color: var(--navy); line-height: 1.5; text-transform: uppercase; }
  .reasons__title { font-size: 7px; font-weight: 700; color: var(--text); margin-bottom: 4px; }
  .reasons { list-style: none; font-size: 6.8px; line-height: 1.4; width: 150px; }
  .reasons li { display: flex; gap: 5px; margin-bottom: 3px; }
  .reasons svg { flex: none; width: 8px; height: 8px; margin-top: 1px; stroke: var(--navy); fill: none; stroke-width: 2; }
</style>
</head>
<body>

<section class="spread spread--outer">
  <article class="page back">
    <div class="brand"><span class="brand__dot"></span><span class="brand__name">BORVENT<br>KÄLTE</span></div>
    <p class="back__address"><strong>BORVENT-KÄLTE</strong><br>Birkenweg 18a<br>A-4817 Tannfeld<br>Österreich</p>
    <p class="back__mail">office@borvent-kaelte.at</p>
  </article>

  <article class="page front">
    <svg class="front__photo" viewBox="0 0 270 250" preserveAspectRatio="none" role="img" aria-label="Foto: modernes Büro mit Wandklimagerät über Holzwand, Tisch und Stühlen">
      <defs>
        <linearGradient id="office" x1="0" y1="0" x2="0" y2="1">
          <stop offset="0" stop-color="#bdbcb8"/>
          <stop offset=".2" stop-color="var(--photo-wall)"/>
          <stop offset=".72" stop-color="#7a5f44"/>
          <stop offset=".75" stop-color="var(--photo-floor)"/>
          <stop offset="1" stop-color="#a5a4a1"/>
        </linearGradient>
      </defs>
      <rect width="270" height="250" fill="url(#office)"/>
    </svg>
    <svg class="front__wedge" viewBox="0 0 270 250" preserveAspectRatio="none" aria-hidden="true">
      <polygon points="0,0 92,0 60,250 0,250" fill="var(--white)"/>
    </svg>
    <div class="brand"><span class="brand__dot"></span><span class="brand__name">BORVENT<br>KÄLTE</span></div>
    <div class="front__band">
      <h1 class="front__title">Klimaanlagen im Gewerbe – sicher, effizient und gesetzeskonform</h1>
      <p class="front__subtitle">Fachgerechte Überprüfung &amp; Reinigung von Klimaanlagen in ganz Österreich</p>
    </div>
  </article>
</section>

<section class="spread spread--inner">
  <article class="page services">
    <h2 class="services__title">Unsere Leistungen im Überblick:</h2>
    <div class="services__grid">
      <div class="service">
        <svg viewBox="0 0 26 22"><rect x="2" y="3" width="18" height="10" rx="2"/><line x1="5" y1="7" x2="15" y2="7"/><circle cx="20" cy="16" r="3.5"/><line x1="22.5" y1="18.5" x2="25" y2="21"/></svg>
        <p class="service__label">Sicht- und Funktionsprüfung (Innen- &amp; Außeneinheit)</p>
      </div>
      <div class="service">
        <svg viewBox="0 0 26 22"><rect x="2" y="3" width="20" height="8" rx="2"/><line x1="5" y1="8" x2="19" y2="8"/><circle cx="7" cy="16" r="1"/><circle cx="12" cy="18" r="1"/><circle cx="17" cy="16" r="1"/></svg>
        <p class="service__label">Reinigung &amp; Desinfektion der Innengeräte</p>
      </div>
      <div class="service">
        <svg viewBox="0 0 26 22"><rect x="4" y="2" width="16" height="18" rx="1"/><line x1="8" y1="2" x2="8" y2="20"/><line x1="12" y1="2" x2="12" y2="20"/><line x1="16" y1="2" x2="16" y2="20"/></svg>
        <p class="service__label">Filterreinigung</p>
      </div>
      <div class="service">
        <svg viewBox="0 0 26 22"><rect x="3" y="3" width="20" height="16" rx="2"/><circle cx="13" cy="11" r="5"/><line x1="13" y1="6" x2="13" y2="16"/><line x1="8" y1="11" x2="18" y2="11"/></svg>
        <p class="service__label">Überprüfung der Ventilatoren (Lager, Rotoren, Verschmutzung)</p>
      </div>
      <div class="service">
        <svg viewBox="0 0 26 22"><rect x="4" y="6" width="7" height="14" rx="1"/><rect x="15" y="6" width="7" height="14" rx="1"/><line x1="7.5" y1="3" x2="7.5" y2="6"/><line x1="18.5" y1="3" x2="18.5" y2="6"/></svg>
        <p class="service__label">Batterietausch bei IR-Fernbedienungen</p>
      </div>
      <div class="service">
        <svg viewBox="0 0 26 22"><rect x="2" y="3" width="20" height="8" rx="2"/><path d="M8 14 l0 5 M13 14 l0 5 M18 14 l0 5"/></svg>
        <p class="service__label">Prüfung der Kondensatabfuhr (inkl. Pumpe &amp; Wanne)</p>
      </div>
      <div class="service">
        <svg viewBox="0 0 26 22"><path d="M13 2 L22 5 V11 C22 16 17 19 13 20 C9 19 4 16 4 11 V5 Z"/><path d="M9 11 l3 3 l5 -6"/></svg>
        <p class="service__label">Überprüfung aller Sicherheitseinrichtungen</p>
      </div>
      <div class="service">
        <svg viewBox="0 0 26 22"><rect x="2" y="4" width="18" height="12" rx="2"/><circle cx="8" cy="10" r="3"/><line x1="13" y1="8" x2="17" y2="8"/><line x1="13" y1="12" x2="17" y2="12"/><path d="M23 4 v10"/><circle cx="23" cy="16" r="2"/></svg>
        <p class="service__label">Dichtheits- &amp; Temperaturprüfung</p>
      </div>
      <div class="service">
        <svg viewBox="0 0 26 22"><circle cx="8" cy="11" r="5"/><circle cx="8" cy="11" r="2"/><path d="M8 6 H22 V16 H8"/></svg>
        <p class="service__label">Kontrolle der Isolierungen &amp; mechanischen Komponenten</p>
      </div>
    </div>
    <p class="footer"><strong>BORVENT-KÄLTE</strong> | Birkenweg 18a | A-4817 Tannfeld | Österreich</p>
  </article>

  <article class="page notice">
    <svg class="notice__photo" viewBox="0 0 270 200" preserveAspectRatio="none" role="img" aria-label="Foto: Reihe von Klima-Außengeräten auf einem Flachdach vor hellem Himmel">
      <defs>
        <linearGradient id="roof" x1="0" y1="0" x2="1" y2="1">
          <stop offset="0" stop-color="var(--white)"/>
          <stop offset=".45" stop-color="var(--photo-sky)"/>
          <stop offset=".8" stop-color="var(--photo-unit)"/>
          <stop offset="1" stop-color="#7f8b95"/>
        </linearGradient>
        <linearGradient id="fade" x1="0" y1="0" x2="1" y2="0">
          <stop offset="0" stop-color="var(--white)"/>
          <stop offset=".5" stop-color="var(--white)" stop-opacity="0"/>
        </linearGradient>
      </defs>
      <rect width="270" height="200" fill="url(#roof)"/>
      <rect width="270" height="200" fill="url(#fade)"/>
    </svg>
    <div class="notice__body">
      <h2 class="notice__title">Hinweis zur gesetzlichen Verpflichtung:</h2>
      <p class="notice__text">Betreiber von Kälte- und Klimaanlagen sind verpflichtet, ihre Anlagen in einem sicheren und hygienisch einwandfreien Zustand zu halten. Die regelmäßige Überprüfung und Reinigung ergibt sich u. a. aus:</p>
      <ul class="laws">
        <li>§ 22 Kälteanlagenverordnung (KAV)</li>
        <li>§ 13 Arbeitsstättenverordnung (AStV)</li>
      </ul>
      <p class="reasons__title">Warum eine regelmäßige Überprüfung wichtig ist:</p>
      <ul class="reasons">
        <li><svg viewBox="0 0 8 8"><path d="M1 4 l2 2 l4 -5"/></svg>Schutz von Mitarbeitenden und Kund:innen</li>
        <li><svg viewBox="0 0 8 8"><path d="M1 4 l2 2 l4 -5"/></svg>Sicherstellung einer hygienisch einwandfreien Luftqualität</li>
        <li><svg viewBox="0 0 8 8"><path d="M1 4 l2 2 l4 -5"/></svg>Vermeidung von Ausfällen und teuren Folgeschäden</li>
        <li><svg viewBox="0 0 8 8"><path d="M1 4 l2 2 l4 -5"/></svg>Erfüllung gesetzlicher Prüf- und Nachweispflichten</li>
      </ul>
    </div>
    <p class="footer footer--right">office@borvent-kaelte.at</p>
  </article>
</section>

</body>
</html>
```